Biker App Design
Zielgruppe
VolmaSen erstellt eine App für Biker mit der:
- Motorradfahrer andere Biker finden können um gemeinsam zu fahren
- Motorradfahrer ihre Strecke tracken können um Punkte zu sammeln
- Biker können mit diesen Punkten Ränge aufsteigen 'Masterbiker, Anfänger, GuruFahrer, etc.', es soll eine Art 'Erfahrungsleiste' angezeigt werden
- Diese Punkte können gegen Gutscheine/Wertsachen eingelöst werden
- Es gibt Nachrichten (Art Blogeinträge) genau zu diesen Themen
Aufgabenstellung
Modernes Design
Reduziert
Es werden folgende Screens benötigt:
Startbild
Start - Dateneintragen:
Um den Fahrer besser mit anderen Fahren zu verknüpfen muss er folgende informationen angeben:
- Welche Art Motorrad fährt er? Sport, Vintage, Cross
- Männlich/Weiblich/Divers
- Geburtsjahr
- PLZ des Heimatorts
- Nickname
Startscreen um andere Biker zu suchen und damit eine Tour zu starten
- Hier sollte ein 'Map' Bild mit einem Kreis für den Umkreis dargestellt werden + Pins mit Personenbilder , welche
Personen in der Nähe sind und auch fahren möchten
- Hier sollte stehen, wieviel Punkte er noch benötigt um den nächsten Gutschein freizuschalten
Screen zum Start des Trackens
Screen während dem Tracken mit Pause/Stop-Option
Screen mit einem Überblick der neuen Blogeinträge
Screen beim beenden des Trackens (Strecke speichern, Bild hinzufügen, Freunde informieren ich bin angekommen)
Screen Profilseite, Bild des Bikers + Bike + Erfahrungspunkte + gesammelte Errungenschaften z.B. 'Mit 3 Freunden mehr als 1000km gefahren'
Screen Bestenliste, anhand der Punkte
Es sollen Dateiformate verwendet werden, die gut wiederverwendet werden können. Es sollen sich Bausteine aus diesen Design wiederverwenden lassen können.

```html
<!DOCTYPE html>
<html lang="en">
<head>
<meta charset="utf-8">
<title>VolmaSen – Leaderboard</title>
<link href="https://fonts.googleapis.com/css2?family=Exo+2:wght@700;800&family=Montserrat:wght@400;700&display=swap" rel="stylesheet">
<style>
  :root{
    --page:#0c141c;
    --screen:#1b252d;
    --statusbar:#141c23;
    --appbar:#1e2931;
    --tag-dark:#151e25;
    --green:#27a63c;
    --white:#ffffff;
    --muted:#6d7a84;
    --icon:#46535d;
    --accent:#e02a2a;
    --divider:#232e36;
  }
  *{box-sizing:border-box;margin:0;padding:0}
  html,body{width:1200px;height:802px;overflow:hidden;background:var(--page)}
  body{font-family:"Montserrat",Arial,sans-serif;color:var(--white)}
  .screen{position:absolute;left:405px;top:11px;width:390px;height:780px;background:var(--screen);overflow:hidden;border-radius:4px}
  .status-bar{height:26px;background:var(--statusbar);display:flex;justify-content:flex-end;align-items:center;gap:6px;padding:0 12px;font-size:13px}
  .app-bar{height:54px;background:var(--appbar);display:flex;align-items:center;padding:0 16px}
  .app-bar .actions{margin-left:auto;display:flex;gap:20px}
  .search-field{height:52px;display:flex;align-items:center;gap:14px;padding:0 24px;color:var(--icon);font-size:15px;border-bottom:1px solid var(--divider)}
  .leaderboard{list-style:none;padding-top:10px}
  .entry{height:74px;display:flex;align-items:center}
  .rank{width:112px;height:46px;display:flex;align-items:center;justify-content:flex-end;padding-right:18px;font-family:"Exo 2",Arial,sans-serif;font-weight:800;font-size:26px;background:var(--tag-dark)}
  .entry.top .rank{background:var(--green)}
  .avatar{width:56px;height:56px;border-radius:50%;margin:0 16px 0 20px;flex:none}
  .rider .name{font-weight:700;font-size:16px}
  .rider .meta{font-size:11px;color:var(--muted);line-height:1.35}
  .bottom-nav{position:absolute;left:0;right:0;bottom:0;height:58px;background:var(--statusbar);display:flex;justify-content:space-around;align-items:center}
  svg{display:block}
</style>
</head>
<body>
<main class="screen">
  <div class="status-bar">
    <svg width="14" height="12" viewBox="0 0 14 12"><path d="M0 0h14L7 12z" fill="#fff"/></svg>
    <svg width="12" height="12" viewBox="0 0 12 12"><path d="M12 0v12H0z" fill="#fff"/></svg>
    <svg width="8" height="13" viewBox="0 0 8 13"><rect x="0" y="1" width="8" height="12" rx="1" fill="#fff"/><rect x="2" y="0" width="4" height="2" fill="#fff"/></svg>
    <span>12:30</span>
  </div>
  <header class="app-bar">
    <svg width="22" height="16" viewBox="0 0 22 16" stroke="var(--icon)" stroke-width="2"><path d="M0 1h22M0 8h22M0 15h22"/></svg>
    <div class="actions">
      <svg width="22" height="22" viewBox="0 0 22 22" fill="none" stroke="var(--icon)" stroke-width="2"><circle cx="9" cy="9" r="7"/><path d="M14 14l7 7"/></svg>
      <svg width="20" height="22" viewBox="0 0 20 22" fill="none" stroke="var(--icon)" stroke-width="2"><path d="M3 16V9a7 7 0 0114 0v7l2 2H1z"/><path d="M8 20h4"/></svg>
      <svg width="22" height="22" viewBox="0 0 22 22" fill="none" stroke="var(--icon)" stroke-width="2"><circle cx="11" cy="11" r="4"/><path d="M11 1v4M11 17v4M1 11h4M17 11h4M4 4l3 3M15 15l3 3M4 18l3-3M15 7l3-3"/></svg>
    </div>
  </header>
  <div class="search-field">
    <svg width="18" height="18" viewBox="0 0 22 22" fill="none" stroke="var(--icon)" stroke-width="2"><circle cx="9" cy="9" r="7"/><path d="M14 14l7 7"/></svg>
    <span>Search Leaderboard</span>
  </div>
  <ol class="leaderboard">
    <li class="entry top"><span class="rank">1st</span><div class="avatar" role="img" aria-label="Rider photo on a sport bike" style="background:radial-gradient(circle,#7a8a6e,#2c3531)"></div><div class="rider"><p class="name">Tom Belardi</p><p class="meta">Sport<br>45 km away from you</p></div></li>
    <li class="entry top"><span class="rank">2nd</span><div class="avatar" role="img" aria-label="Rider photo with helmet" style="background:radial-gradient(circle,#c9d2da,#4c5a66)"></div><div class="rider"><p class="name">Rainer Holst</p><p class="meta">Sport<br>45 km away from you</p></div></li>
    <li class="entry top"><span class="rank">3rd</span><div class="avatar" role="img" aria-label="Black and white motorcycle photo" style="background:radial-gradient(circle,#e6e6e6,#3a3a3a)"></div><div class="rider"><p class="name">Rudi Vanterk</p><p class="meta">Sport<br>45 km away from you</p></div></li>
    <li class="entry"><span class="rank">4th</span><div class="avatar" role="img" aria-label="Motorcycle detail photo" style="background:radial-gradient(circle,#9aa1a8,#2f3439)"></div><div class="rider"><p class="name">Ramon Esquibel</p><p class="meta">Sport<br>45 km away from you</p></div></li>
    <li class="entry"><span class="rank">5th</span><div class="avatar" role="img" aria-label="Rider on a red cross bike" style="background:radial-gradient(circle,#c0c8d4,#7a3b3b)"></div><div class="rider"><p class="name">Mirko Tavelic</p><p class="meta">Sport<br>45 km away from you</p></div></li>
    <li class="entry"><span class="rank">6th</span><div class="avatar" role="img" aria-label="Rider on the road" style="background:radial-gradient(circle,#d5dde3,#4a525a)"></div><div class="rider"><p class="name">Stepan Korvalin</p><p class="meta">Sport<br>45 km away from you</p></div></li>
    <li class="entry"><span class="rank">7th</span><div class="avatar" role="img" aria-label="Rider in a field" style="background:radial-gradient(circle,#c8cfc4,#4f5d44)"></div><div class="rider"><p class="name">Max Von Lerda</p><p class="meta">Sport<br>45 km away from you</p></div></li>
    <li class="entry"><span class="rank">8th</span><div class="avatar" role="img" aria-label="Blue motorcycle photo" style="background:radial-gradient(circle,#e0e8f0,#3d5f8a)"></div><div class="rider"><p class="name">Selma Ortani</p><p class="meta">Sport<br>45 km away from you</p></div></li>
  </ol>
  <nav class="bottom-nav">
    <svg width="24" height="22" viewBox="0 0 24 22" fill="none" stroke="var(--icon)" stroke-width="2"><path d="M1 3l7-2 8 3 7-2v17l-7 2-8-3-7 2z"/><path d="M8 1v17M16 4v17"/></svg>
    <svg width="22" height="24" viewBox="0 0 22 24" fill="none" stroke="var(--accent)" stroke-width="2"><path d="M3 23V1h16l-4 6 4 6H3"/></svg>
    <svg width="24" height="24" viewBox="0 0 24 24" fill="none" stroke="var(--icon)" stroke-width="2"><circle cx="12" cy="12" r="10"/></svg>
    <svg width="24" height="22" viewBox="0 0 24 22" fill="none" stroke="var(--icon)" stroke-width="2"><rect x="1" y="6" width="17" height="15" rx="2"/><path d="M6 1h15a2 2 0 012 2v12"/></svg>
    <svg width="22" height="24" viewBox="0 0 22 24" fill="none" stroke="var(--icon)" stroke-width="2"><circle cx="11" cy="7" r="5"/><path d="M1 23c0-6 4-9 10-9s10 3 10 9"/></svg>
  </nav>
</main>
</body>
</html>
```